Our business deals with residential and commercial property management. We have commercial tenants willing to offer deals to our residential tenants. We want a very nice looking card stock where I can add (later) each specific deal/incentive. The template attached has two options but feel free to come up with what you think looks best. We need or logo and possibly this simple phrase as the title,

"Welcome to the Brelford Community!" OR "Join the Brelford Community"

This is optional, use discretion on what is should say:

"Every member of Brelford Commercial is important to us, be a part of our community and explore your neighborhood."

www.brelfordcommercial.example can give you a feel for our look and image. I was thinking of maybe a red & black color scheme.

***Each slot for the deal should be blank so I can add and change each deal later. These are going to be cut out so maybe the "-----" lines around the deals would look good. Thanks!!

Target Market(s)

Residential Tenants: Single & Multi Families

Industry/Entity Type

Property Management

Font styles to use
Serif

Colors
ec1f27
000000
fbfbfb

Requirements
Must have
• -Logo (Attached)
• -6 blank slots to add deals later (Can have more deals based on appropriate look)
• -either "Welcome to the Brelford Community" or "Join the Brelford Community"
• -Our phone number: 801.555.0147
• -Website: www.brelfordcommercial.example
• -Address: 417 E. Dunmore Way Suite 5, Centerville, UT 84099
Nice to have
• "Every member of Brelford Commercial is important to us, be a part of our community and explore your neighborhood."
• This could be something else that's similar but sounds better.
• Possible color options: red, black, white OR Your discretion.
Should not have
• Pictures of properties or people.

```html
<!DOCTYPE html>
<html lang="en">
<head>
<meta charset="utf-8">
<title>Welcome to the Brelford Community</title>
<link href="https://fonts.googleapis.com/css2?family=Open+Sans:ital,wght@0,400;0,600;0,700;1,400;1,600&display=swap" rel="stylesheet">
<style>
  :root{
    --red:#ec1f27;
    --slot-red:#a3141b;
    --black:#000000;
    --paper:#fbfbfb;
    --grey:#6d6e71;
    --white:#ffffff;
  }
  *{box-sizing:border-box;margin:0;padding:0}
  html,body{width:849px;height:1200px;overflow:hidden;background:var(--paper)}
  body{font-family:"Open Sans",Arial,sans-serif;color:var(--black)}
  .card{position:relative;width:849px;height:1200px;background:var(--paper);overflow:hidden}
  .corner{position:absolute;left:0;top:0}
  .site-band{position:absolute;top:0;left:262px;right:0;height:34px;background:var(--red);
    color:var(--white);font-size:14px;letter-spacing:3px;font-weight:600;
    display:flex;align-items:center;justify-content:flex-end;padding-right:62px}
  .brand{position:absolute;top:118px;right:44px;display:flex;align-items:center;gap:12px}
  .brand-mark{width:22px;height:22px;background:var(--red)}
  .brand-name{font-size:30px;font-weight:600;color:var(--black)}
  .headline{position:absolute;top:222px;left:297px;width:520px}
  .headline .lead{font-size:44px;font-weight:400;color:#333;line-height:1.15}
  .headline .name{font-size:43px;font-weight:700;line-height:1.2;white-space:nowrap}
  .headline .name .accent{color:var(--red)}
  .intro{position:absolute;top:350px;left:235px;width:572px;text-align:center;font-size:16.5px;color:var(--grey);line-height:1.35}
  .deals{position:absolute;top:468px;left:34px;width:772px;display:grid;
    grid-template-columns:repeat(4,1fr);grid-template-rows:122px 122px;gap:42px 24px}
  .deal-slot{background:var(--slot-red);outline:2px dashed var(--slot-red);outline-offset:6px}
  .todo-label{position:absolute;top:820px;left:34px;background:var(--black);color:var(--white);
    font-size:24px;font-weight:600;padding:5px 22px}
  .todo{position:absolute;top:878px;left:52px;list-style:none;font-size:15px;line-height:31px}
  .todo li::before{content:"•";margin-right:10px}
  .contact{position:absolute;top:1046px;left:612px;color:var(--red);font-style:italic}
  .contact h2{font-size:29px;font-weight:600}
  .contact .phone{font-size:21px;margin-top:6px}
  .contact address{font-style:normal;color:var(--black);font-size:13px;line-height:1.45;margin-top:8px;width:200px}
</style>
</head>
<body>
<main class="card">
  <svg class="corner" width="270" height="400" viewBox="0 0 270 400" aria-hidden="true">
    <polygon points="0,0 258,0 0,390" fill="#000000"/>
  </svg>
  <div class="site-band">www.brelfordcommercial.example</div>

  <div class="brand"><span class="brand-mark"></span><span class="brand-name">Brelford Commercial</span></div>

  <header class="headline">
    <p class="lead">Welcome to the</p>
    <h1 class="name"><span class="accent">BRELFORD</span> COMMUNITY!</h1>
  </header>
  <p class="intro">Every member of Brelford Commercial is important to us,<br>be a part of our community and explore your neighborhood.</p>

  <section class="deals" aria-label="Deal slots">
    <div class="deal-slot"></div>
    <div class="deal-slot"></div>
    <div class="deal-slot"></div>
    <div class="deal-slot"></div>
    <div class="deal-slot"></div>
    <div class="deal-slot"></div>
    <div class="deal-slot"></div>
    <div class="deal-slot"></div>
  </section>

  <div class="todo-label">Deals to implement:</div>
  <ul class="todo">
    <li>Brelford's: ____</li>
    <li>Hollow Oak:- ____</li>
    <li>Comet: ____</li>
    <li>Summit Ridge mortgage: ____</li>
    <li>Ashbrook: ____</li>
    <li>Nonna's: ____</li>
  </ul>

  <section class="contact">
    <h2>Contact Us:</h2>
    <p class="phone">Phone: 801.555.0147</p>
    <address>Address: 417 E. Dunmore Way Suite 5, Centerville, UT 84099</address>
  </section>
</main>
</body>
</html>
```